Corvane Photography Business Card Design

I need a business card designed for a photography business based in Perth, Western Australia called Corvane Photography.

We specialise in wedding, event photography and portrait photography.

The business card must borrow the style of the attached logo.

The hex codes for the colours in the logo are:
#ED1D85 - Pink
#89C23E - Green
#37282F - Black

The name on the card will be:
Name: Teodric
Phone: 0417360825
Website: www.corvanephotography-example.com.au
Facebook: corvanephotography

I am open and happy to accept creative concepts.

Industry/Entity Type

Business

```html
<!DOCTYPE html>
<html lang="en">
<head>
<meta charset="utf-8">
<title>Corvane Photography – Business Card</title>
<link rel="stylesheet" href="https://fonts.googleapis.com/css2?family=Questrial&family=Share+Tech+Mono&display=swap">
<style>
  :root {
    --page: #ffffff;
    --guide: #8fe6ef;
    --ink: #37282f;
    --pink: #ed1d85;
    --magenta: #fb1fec;
    --green: #89c23e;
    --white: #ffffff;
  }
  * { margin: 0; padding: 0; box-sizing: border-box; }
  html, body {
    width: 1000px;
    height: 1200px;
    overflow: hidden;
    background: var(--page);
  }
  .canvas {
    position: relative;
    width: 1000px;
    height: 1200px;
  }
  .card {
    position: absolute;
    left: 127px;
    width: 740px;
    height: 440px;
    border: 1px solid var(--guide);
    overflow: hidden;
  }
  .card--front { top: 64px; background: var(--white); }
  .card--back  { top: 680px; background: var(--magenta); }

  /* front */
  .front-mark {
    position: absolute;
    left: 290px;
    top: 134px;
    width: 158px;
    height: 158px;
  }
  .front-name {
    position: absolute;
    left: 0;
    right: 0;
    top: 329px;
    text-align: center;
    font-family: "Questrial", sans-serif;
    font-size: 23px;
    letter-spacing: 0.52em;
    text-indent: 0.52em;
    color: var(--ink);
    text-transform: uppercase;
  }

  /* back */
  .back-text {
    font-family: "Share Tech Mono", monospace;
    color: var(--white);
    text-transform: uppercase;
    letter-spacing: 0.16em;
  }
  .services {
    position: absolute;
    left: 66px;
    top: 118px;
    list-style: none;
    font-size: 19px;
    line-height: 30px;
  }
  .back-brand {
    position: absolute;
    left: 66px;
    top: 212px;
    display: flex;
    align-items: center;
    gap: 10px;
    font-size: 13px;
    letter-spacing: 0.12em;
  }
  .back-brand__dot {
    width: 40px;
    height: 40px;
    border-radius: 50%;
    background: var(--white);
    flex: none;
  }
  .contact {
    position: absolute;
    left: 66px;
    top: 308px;
    list-style: none;
    font-size: 16px;
    line-height: 24px;
    text-transform: none;
    font-variant: small-caps;
    letter-spacing: 0.12em;
  }
  .petal-artwork {
    position: absolute;
    right: 0;
    top: 0;
    width: 202px;
    height: 100%;
    background: linear-gradient(160deg, #ffffff 0%, #c9f29a 35%, #ffffff 60%, #89c23e 80%, #ffffff 100%);
    opacity: 0.9;
  }
</style>
</head>
<body>
<div class="canvas">

  <section class="card card--front">
    <svg class="front-mark" viewBox="0 0 158 158" aria-hidden="true">
      <circle cx="79" cy="79" r="78" fill="var(--pink)"/>
    </svg>
    <p class="front-name">Corvane Photography</p>
  </section>

  <section class="card card--back">
    <ul class="services back-text">
      <li>Wedding</li>
      <li>Event Photography</li>
      <li>Portrait Photography•••</li>
    </ul>

    <div class="back-brand back-text">
      <span class="back-brand__dot"></span>
      <span>Corvane</span>
    </div>

    <ul class="contact back-text">
      <li>Teodric</li>
      <li>Phone: 0417360825</li>
      <li>Website: www.corvanephotography-example.com.au</li>
      <li>Facebook: corvanephotography</li>
    </ul>

    <div class="petal-artwork" role="img" aria-label="Large decorative petal pattern in white, green and dark tones"></div>
  </section>

</div>
</body>
</html>
```